Policy Manual in Education

I need the attached document to be put in a publishable format, with graphics a professional layout, and something that looks more like a professional report, etc. Use color samples from http://www.brwt-qx.com/ and www.kv7lo.com, my company is Kv7lo, we were hired to write the report and we also built the BRWT resource center http://www.brwt-qx.com/ .

Target Market(s)

Education

Requirements
Must have
• Look and feel around NM. http://www.brwt-qx.com/ and www.kv7lo.com

```html
<!DOCTYPE html>
<html lang="en">
<head>
<meta charset="utf-8">
<title>Education Policy Report – Page Spreads</title>
<link href="https://fonts.googleapis.com/css2?family=Open+Sans:wght@300;400;600;700;800&display=swap" rel="stylesheet">
<style>
:root{
  --backdrop:#b3b3b3;
  --paper:#ffffff;
  --navy:#1b3a6f;
  --blue:#1f5aa0;
  --blue-light:#2d6fb8;
  --orange:#f9a51b;
  --orange-deep:#f08a12;
  --ink:#2b2b2b;
  --muted:#555;
  --row-blue:#cfe3f3;
  --row-grey:#e2e2e2;
}
*{margin:0;padding:0;box-sizing:border-box}
html,body{width:1200px;height:1200px;overflow:hidden;background:var(--backdrop);font-family:"Open Sans",Arial,sans-serif;color:var(--ink)}
.page{position:absolute;width:258px;height:350px;background:var(--paper);overflow:hidden;box-shadow:0 1px 3px rgba(0,0,0,.25)}
.cover svg{position:absolute;left:0;top:0}
.brand{font-weight:800;color:var(--navy);letter-spacing:.5px;white-space:nowrap}
.brand .dot{display:inline-block;width:.8em;height:.8em;background:var(--orange);margin-right:.3em;vertical-align:-.05em}
.run-head{position:absolute;left:28px;right:28px;top:24px;text-align:center;border-top:1px dotted var(--blue);border-bottom:1px dotted var(--blue);padding:5px 0 3px;font-size:8.5px;letter-spacing:.3px;color:#222;text-transform:uppercase}
.run-foot{position:absolute;left:22px;right:14px;bottom:13px;display:flex;align-items:center;gap:6px}
.run-foot .brand{font-size:6.5px}
.run-foot .rule{flex:1;height:1px;background:var(--navy)}
.run-foot .num{font-size:5.5px;color:var(--blue)}
.body{position:absolute;left:26px;right:22px;top:52px;font-size:3.9px;line-height:1.55;color:var(--ink)}
.body p{margin-bottom:4px}
.body h3{font-size:7px;color:var(--blue);font-weight:600;margin:5px 0 2px}
.body .sub{color:var(--blue);font-size:3.9px}
.body .lead{color:var(--blue)}
.body ul{list-style:none;margin-bottom:4px}
.body li{padding-left:9px;position:relative;color:var(--blue)}
.body li::before{content:"▶";position:absolute;left:2px;font-size:3.5px}
.body li.sq{color:var(--ink);padding-left:4px}
.body li.sq::before{content:"■";left:0}
.toc{width:100%;font-size:3.8px;border-collapse:collapse}
.toc td{padding:1px 0}
.toc .dots{border-bottom:1px dotted #888;width:70%}
.toc .pg{text-align:right}
.grid{width:100%;border-collapse:separate;border-spacing:1px;font-size:3.6px;margin:4px 0 6px}
.grid th{background:var(--navy);color:#fff;font-weight:600;padding:1px}
.grid td{background:var(--row-grey);padding:1px 4px}
.grid td.c{text-align:center}
.grid tr.phase td{background:var(--row-blue);color:var(--blue);font-weight:600}
.grid tr.total td{background:var(--blue-light);color:#fff;font-weight:600}
.callout{display:flex;align-items:center;background:var(--navy);color:#fff;font-size:3.9px;line-height:1.4;margin-bottom:6px}
.callout .badge{width:26px;height:22px;background:var(--orange);display:flex;align-items:center;justify-content:center}
.callout .badge span{width:12px;height:12px;border:1.5px solid #fff;border-radius:50%}
.callout p{padding:2px 6px;margin:0}
.photo{background:linear-gradient(135deg,#2a3346,#6a7488 55%,#c9c4bb)}
</style>
</head>
<body>

<!-- Front cover -->
<section class="page cover" style="left:54px;top:32px">
  <svg width="258" height="350" viewBox="0 0 258 350">
    <defs><linearGradient id="coverBlue" x1="0" y1="0" x2="0" y2="1"><stop offset="0" stop-color="#1f5aa0"/><stop offset="1" stop-color="#1b3a6f"/></linearGradient></defs>
    <rect width="258" height="350" fill="url(#coverBlue)"/>
    <polygon points="0,284 258,190 258,350 0,350" fill="#f9a51b"/>
    <polygon points="0,316 258,236 258,350 0,350" fill="#fff"/>
  </svg>
  <div class="brand" style="position:absolute;left:118px;top:295px;font-size:11px"><span class="dot"></span>Halvern Education</div>
</section>

<!-- Inside title -->
<section class="page" style="left:348px;top:32px">
  <div class="brand" style="position:absolute;left:0;right:0;top:64px;text-align:center;font-size:15px"><span class="dot"></span>Halvern Education</div>
  <div style="position:absolute;left:0;right:0;top:150px;height:10px;background:linear-gradient(var(--orange),var(--orange-deep))"></div>
  <div style="position:absolute;left:0;right:0;top:160px;bottom:0;background:linear-gradient(#1f5aa0,#1b3a6f)"></div>
  <div style="position:absolute;left:0;right:0;top:212px;text-align:center;color:#fff;font-weight:300;font-size:13.5px;line-height:1.5">LOREM IPSUM IS SIMPLY<br>DUMMY HAS BEEN</div>
</section>

<!-- Table of contents -->
<section class="page" style="left:635px;top:32px">
  <div class="run-head">Table of Contents</div>
  <div class="body" style="top:50px">
    <h3 style="font-size:6.5px">Contents</h3>
    <table class="toc">
      <tr><td>Table of Contents</td><td class="dots"></td><td class="pg">01</td></tr>
      <tr><td>Executive Summary</td><td class="dots"></td><td class="pg">02</td></tr>
      <tr><td>Our Understanding of Your Needs</td><td class="dots"></td><td class="pg">02</td></tr>
      <tr><td>Our Recommendations</td><td class="dots"></td><td class="pg">03</td></tr>
      <tr><td>Our Approach</td><td class="dots"></td><td class="pg">05</td></tr>
      <tr><td>Budget and Timeframe</td><td class="dots"></td><td class="pg">07</td></tr>
      <tr><td>Appendix A: About Alder Creek</td><td class="dots"></td><td class="pg">10</td></tr>
      <tr><td>Appendix B: Selected Client List</td><td class="dots"></td><td class="pg">10</td></tr>
      <tr><td>Appendix C: Our Capabilities</td><td class="dots"></td><td class="pg">11</td></tr>
      <tr><td>Appendix D: Our Process</td><td class="dots"></td><td class="pg">12</td></tr>
    </table>
  </div>
  <div class="run-foot"><span class="brand">Halvern</span><span class="rule"></span><span class="num">01</span></div>
</section>

<!-- Solution page -->
<section class="page" style="left:922px;top:32px">
  <div class="run-head">Headline Here</div>
  <div class="body" style="top:46px">
    <h3>Solution</h3>
    <p><span class="sub">AI automated accounting</span><br>Ledgerly builds automation in stages on top of its current system to reach full automation. It connects to all sources of accounting data such as bank accounts, credit cards, webshop or document storage. Based on this data, Ledgerly creates bookings and generates financial reports, and a chat interface lets users talk to it as a trusted advisor over time.</p>
    <p><span class="sub">Blockchain software license or Token-as-a-License</span><br>It is possible to create tokens on a blockchain that represent software licenses. Ledgerly creates tokens on the Kestrel chain. Upon purchase, the token holder is free to transfer or sell it using a secondary market built directly over the chain. Ledgerly checks the validity of a token against the chain, ensuring that token holders have access to the software. This makes distribution and resale of licenses easier for developers and owners alike.</p>
    <h3>Pre-ICO Token sale</h3>
    <p>To realize this vision, Ledgerly is launching a pre-ICO in the form of a token sale. 20,000,000 tokens are available for purchase during a 30-day period to be announced. Tokens represent lifelong software licenses. Future customers will still have the option to buy directly yearly or monthly subscriptions.</p>
    <h3>Future plans</h3>
    <p>A future ICO is planned between 18 and 24 months after the pre-ICO token sale. This offering will support the development of Ledgerly into a fully decentralized, privacy-focused ecosystem of applications where zero administrative tasks becomes reality.</p>
  </div>
  <div class="run-foot"><span class="brand">Halvern</span><span class="rule"></span><span class="num">02</span></div>
</section>

<!-- Vision -->
<section class="page" style="left:54px;top:416px">
  <div class="run-head">Vision</div>
  <div class="body" style="top:45px">
    <div class="callout"><div class="badge"><span></span></div><p>Ledgerly's mission is to help and support the self-employed and small business owners with their administrative tasks so they can focus on what matters – their business.</p></div>
    <p class="lead">Administrative tasks are cumbersome, time-consuming and often prevent small owners from focusing their time and energy on their business and their customers.</p>
    <p style="text-align:center">At Ledgerly, we envisage accounting for the self-employed and small business owners as being <span class="lead">automated and decentralized</span></p>
    <p>Accounting can and should be done automatically. By connecting to all sources of accounting data such as bank accounts, payment systems and invoicing systems, Ledgerly completes these tasks which would take hours to do manually. Reports are available within a couple of clicks.</p>
    <p>What may seem like a pipedream to the millions of self-employed who struggle with their admin is already a reality. Now is the time to join Ledgerly on its mission.</p>
    <h3>The Ledgerly model</h3>
    <p>Ledgerly is based on an innovative license model that uses Token-as-a-License. The token represents lifelong software license for Ledgerly solutions. The pre-ICO token sale will enable Ledgerly to complete its development of AI bookkeeping.</p>
    <p>The pre-ICO token sale will also pave the way for a future ICO. Ledgerly will launch accounting on the blockchain and ensure your accounting data is comprehensive and private, available everywhere within your preferred apps.</p>
    <p>Ledgerly supports strong data ownership laws that truly protect individuals and ensure they have complete ownership of their data.</p>
    <p>To find out more about the Ledgerly AI project, please register with your email at <span class="lead">www.ledgerly-ai.com</span> so we can keep you informed.</p>
  </div>
  <div class="run-foot"><span class="brand">Halvern</span><span class="rule"></span><span class="num">03</span></div>
</section>

<!-- Budget -->
<section class="page" style="left:348px;top:416px">
  <div class="run-head">Budget and Timeframe</div>
  <div class="body" style="top:46px">
    <h3>Implementation Estimate</h3>
    <p>The bulk of the implementation costs will be defined by discovery. Based on similar CRM implementation projects, we feel expect the CRM side will be something between 200 and 300 hours. The wide swing in hours in phase one is related to the undefined nature of both the integration needs and our role in the integration project.</p>
    <table class="grid">
      <tr><th>Task</th><th>Hours</th><th>Cost</th></tr>
      <tr><td>Discovery</td><td class="c">40</td><td class="c">$8,000</td></tr>
      <tr class="phase"><td>Phase 1</td><td></td><td></td></tr>
      <tr><td>Discovery</td><td class="c">20-40</td><td class="c">$8,000</td></tr>
      <tr><td>Discovery</td><td class="c">20-40</td><td class="c">$8,000</td></tr>
      <tr><td>Discovery</td><td class="c">20-40</td><td class="c">$8,000</td></tr>
      <tr><td>Total Phase 1</td><td class="c">80-240</td><td class="c">$16,800-40,000</td></tr>
      <tr class="phase"><td>Phase 2</td><td></td><td></td></tr>
      <tr><td>Discovery</td><td class="c">20-40</td><td class="c">$8,000</td></tr>
      <tr><td>Total Phase 2</td><td class="c">80-240</td><td class="c">$16,800-40,000</td></tr>
      <tr class="total"><td>Total Estimated Implementation Cost</td><td class="c">220-480</td><td class="c">$44,000-96,000</td></tr>
    </table>
    <h3>Project Timeline</h3>
    <p>Based on the information we have at our disposal, the March 21st launch date doesn't seem realistic given the work needed to provide the foundation for the future CRM instance. We are currently estimating that the first phase will take somewhere between 7 and 12 weeks.</p>
    <table class="grid">
      <tr><th>Task</th><th>Weeks to Complete</th></tr>
      <tr><td>Discovery</td><td class="c">1-2</td></tr>
      <tr><td>Phase 1</td><td class="c">6-10</td></tr>
      <tr><td>Phase 2</td><td class="c">8-12</td></tr>
      <tr><td>Total Number of Weeks</td><td class="c"></td></tr>
    </table>
  </div>
  <div class="run-foot"><span class="brand">Halvern</span><span class="rule"></span><span class="num">04</span></div>
</section>

<!-- Understanding -->
<section class="page" style="left:635px;top:416px">
  <div class="run-head">Our Understanding of Your Needs</div>
  <div class="body" style="top:46px">
    <p>In the last two weeks of January we conducted high level conversations both with your staff and your technology partner SignalWorks. As a result of those conversations we've been able to gather the following high level goals for your project:</p>
    <p style="font-size:5.6px;color:#666;line-height:1.35">The CRM platform must be in place to support Waypoint at launch and as the program evolves</p>
    <p class="lead" style="font-weight:600">The most critical aspect of this implementation lies in time sensitivity as well as functionality centered around support for the Waypoint project.</p>
    <ul>
      <li class="sq">Waypoint will be comprised of a series of websites focused on organizing institutions and individuals within specific community sectors to support America in minimizing risks.</li>
      <li class="sq">The primary goals of the CRM application are:</li>
      <li>capture information of individuals and organizations</li>
      <li>track their progress on their site specific to-do lists</li>
      <li>allow GreenCivic to push out next steps to their progress</li>
      <li>infuse GreenCivic's online and offline marketing program with useful segmentation</li>
      <li>natively integrate with the Waypoint family of sites</li>
    </ul>
    <ul>
      <li class="sq">The data architecture must be well defined but flexible to support the core needs of the sites.</li>
      <li>For instance, the faith based site may collect a "denomination" field while others may not.</li>
      <li>Future interactions outside of the to-do list may become necessary to track and GreenCivic will need a systemic way to capture them.</li>
    </ul>
    <ul><li class="sq">The information collected from the Waypoint sites must be combined with existing information held within GreenCivic for a holistic view.</li></ul>
  </div>
  <div class="run-foot"><span class="brand">Halvern</span><span class="rule"></span><span class="num">06</span></div>
</section>

<!-- Headline with banner image -->
<section class="page" style="left:922px;top:416px">
  <div class="run-head">Headline Here</div>
  <div class="photo" role="img" aria-label="Photo of a stressed businessman at a desk" style="position:absolute;left:29px;right:22px;top:44px;height:88px"></div>
  <div class="body" style="top:138px">
    <p class="lead">Ledgerly's mission is to help and support the self-employed and small business owners with their administrative tasks so they can focus on what matters – their business.</p>
    <p>Administrative tasks are cumbersome, time-consuming and often prevent small owners from focusing their time and energy on their business and their customers.</p>
    <p>At Ledgerly, we envisage accounting for the self-employed and small business owners as being <span class="lead">automated and decentralized</span></p>
    <p>Accounting can and should be done automatically. By connecting to all sources of accounting data, Ledgerly completes tasks which would take hours to do manually, and will offer tips to improve financial stability.</p>
    <p>What may seem like a pipedream to the millions of self-employed is already a reality. Now is the time to join Ledgerly on its mission.</p>
    <h3>The Ledgerly model</h3>
    <p>Ledgerly is based on an innovative license model that uses Token-as-a-License. The token represents lifelong software license for Ledgerly solutions.</p>
    <p>with leading edge business data access to ensure you have the best available data at your fingertips.</p>
  </div>
  <div class="run-foot"><span class="brand">Halvern</span><span class="rule"></span><span class="num">07</span></div>
</section>

<!-- Headline with side images -->
<section class="page" style="left:54px;top:800px">
  <div class="run-head">Headline Here</div>
  <div class="photo" role="img" aria-label="Photo of a businessman holding his head at a desk" style="position:absolute;left:27px;top:44px;width:90px;height:130px"></div>
  <div class="photo" role="img" aria-label="Photo of a businessman in a suit reading documents" style="position:absolute;left:27px;top:197px;width:90px;height:116px;background:linear-gradient(135deg,#3a2c25,#7d6a5d 55%,#d8d2c8)"></div>
  <div class="body" style="left:129px;top:44px">
    <p class="lead">Ledgerly's mission is to help and support the self-employed and small business owners with their administrative tasks so they can focus on what matters – their business.</p>
    <p>Administrative tasks are cumbersome, time-consuming and often prevent small owners from focusing their time and energy on their business and their customers. They can also be stressful for those attempting these tasks for the first time.</p>
    <p>At Ledgerly, we envisage accounting for the self-employed and small business owners as being <span class="lead">automated and decentralized</span></p>
    <p>Accounting can and should be done automatically. By connecting to all sources of accounting data such as bank accounts, payment systems and invoicing systems, Ledgerly completes these tasks, which would take hours to do manually. Statements are available within a couple of clicks, and Ledgerly will offer tips to improve your financial stability.</p>
    <p>What may seem like a pipedream to the millions of self-employed who struggle with</p>
    <h3>The Ledgerly model</h3>
    <p>Ledgerly is based on an innovative license model that uses Token-as-a-License. The token represents lifelong software license for Ledgerly solutions. The pre-ICO token sale will enable Ledgerly to complete its development of AI to deliver fully automatic bookkeeping.</p>
  </div>
  <div class="run-foot"><span class="brand">Halvern</span><span class="rule"></span><span class="num">08</span></div>
</section>

<!-- Back cover -->
<section class="page cover" style="left:348px;top:800px">
  <svg width="258" height="350" viewBox="0 0 258 350">
    <defs><linearGradient id="backBlue" x1="0" y1="0" x2="0" y2="1"><stop offset="0" stop-color="#1f5aa0"/><stop offset="1" stop-color="#1b3a6f"/></linearGradient></defs>
    <rect width="258" height="350" fill="url(#backBlue)"/>
    <polygon points="0,282 258,202 258,350 0,350" fill="#f9a51b"/>
    <polygon points="0,296 258,238 258,350 0,350" fill="#fff"/>
  </svg>
  <div class="brand" style="position:absolute;left:46px;top:306px;font-size:9px"><span class="dot"></span>Halvern</div>
  <div style="position:absolute;left:104px;top:303px;font-size:3.4px;line-height:1.7;color:var(--navy)">
    <div>☎ 000-555-0142 Ext 101</div>
    <div>✉ office@halvern-ed.org</div>
    <div>⌂ www.halvern-ed.org</div>
  </div>
  <div style="position:absolute;left:160px;top:305px;font-size:3.4px;line-height:1.7;color:var(--navy);border-left:1px solid var(--navy);padding-left:4px">
    <div>210 Mesa Ridge Road</div>
    <div>Santa Rosa, NM 87500</div>
  </div>
</section>

</body>
</html>
```